New Business Card Design Project VORASTI-Italy

we are VORASTI-Italy
our company in the market for 3 years we are luxury cosmetic company and its about time for a facelift :)
i will like to have elegant luxurious and unique business card
that will give the person that get it a unique, luxurious and elegant impression
I'm VERY OPEN FOR NEW IDEAS , even duo i add a few files of things that i see on line and i like them

i add my logo as well
my website is VORASTI.COM
(if you would like to see the main style that we have)

Target Market(s)

adult that have money :)

Industry/Entity Type

Business

Contact Information for Business Card

Name - Paul Vorasti
Position - CEO and CO Founder
address - 4817 E Larkdale
telephone - 555-384-1962
email - paul@vorasti.com
fax - 555-384-1962
website - VORASTI.COM

Colors
000000
959595
fbee3e
ffffff

Requirements
Must have
• big logo in GOLD color
• elegant look
• impressive
Nice to have
• not must but maybe classy pattern background
• not must but maybe emblem
• maybe clear plastic business card
Should not have
• colors
• images

```html
<!DOCTYPE html>
<html lang="en">
<head>
<meta charset="utf-8">
<title>VORASTI Italy – Business Card</title>
<link rel="stylesheet" href="https://fonts.googleapis.com/css2?family=Marcellus&family=Lato:wght@400;700&family=Oswald:wght@500&display=swap">
<style>
  :root {
    --stage: #2b2b2c;
    --card-dark: #2a2623;
    --card-dark-deep: #201d1b;
    --gold: #c9ac6a;
    --gold-light: #e4cf92;
    --gold-deep: #a88a4a;
    --ink: #1e1a17;
  }
  * { margin: 0; padding: 0; box-sizing: border-box; }
  html, body {
    width: 1200px; height: 901px; overflow: hidden;
    background: var(--stage);
  }
  .stage {
    width: 1200px; height: 901px;
    display: flex; flex-direction: column;
    align-items: center; justify-content: center; gap: 44px;
  }
  .card {
    position: relative; width: 600px; height: 343px;
    border-radius: 4px; overflow: hidden;
    box-shadow: 0 14px 30px rgba(0,0,0,.45);
  }
  .card__texture { position: absolute; inset: 0; }

  /* Front */
  .card--front .card__texture {
    background: linear-gradient(135deg, var(--gold-deep) 0%, var(--gold-light) 45%, var(--gold) 70%, var(--gold-deep) 100%);
  }
  .front__mark {
    position: absolute; left: 0; right: 0; top: 0; height: 205px;
    display: flex; align-items: center; justify-content: center; gap: 14px;
  }
  .mark__dot {
    width: 26px; height: 26px; border-radius: 50%;
    border: 2px solid var(--ink);
  }
  .mark__name {
    font-family: "Marcellus", serif; font-size: 30px; letter-spacing: 4px;
    color: var(--ink);
  }
  .front__band {
    position: absolute; left: 0; right: 0; bottom: 0; height: 138px;
    background: var(--card-dark);
    display: flex; flex-direction: column; align-items: center; justify-content: center;
  }
  .wordmark {
    font-family: "Marcellus", serif; font-size: 44px; letter-spacing: 4px;
    color: var(--gold);
    padding: 0 14px 6px; border-bottom: 2px solid var(--gold);
  }
  .wordmark__place {
    margin-top: 8px;
    font-family: "Marcellus", serif; font-size: 15px; letter-spacing: 4px;
    color: var(--gold);
  }

  /* Back */
  .card--back .card__texture {
    background: linear-gradient(135deg, var(--card-dark) 0%, var(--card-dark-deep) 100%);
  }
  .back__layout {
    position: absolute; inset: 0;
    display: flex; align-items: center; padding: 0 52px; gap: 46px;
  }
  .identity { display: flex; flex-direction: column; align-items: flex-start; }
  .identity .mark__dot { border-color: var(--gold); width: 34px; height: 34px; }
  .identity__mark { display: flex; align-items: center; gap: 12px; margin-bottom: 30px; }
  .identity .mark__name { color: var(--gold); font-size: 28px; }
  .identity__person {
    font-family: "Oswald", sans-serif; font-weight: 500; font-size: 30px;
    color: var(--gold); letter-spacing: 1px; text-transform: uppercase; line-height: 1.05;
  }
  .identity__role {
    font-family: "Lato", sans-serif; font-size: 16px; color: var(--gold); margin-top: 4px;
  }
  .contacts { list-style: none; display: flex; flex-direction: column; gap: 13px; }
  .contacts__item {
    display: flex; align-items: center; gap: 12px;
    font-family: "Lato", sans-serif; font-size: 16px; color: var(--gold);
  }
  .contacts__item::before {
    content: ""; width: 8px; height: 8px; background: var(--gold); flex: none;
  }
  .contacts__item--plain::before { background: transparent; }
</style>
</head>
<body>
<main class="stage">
  <section class="card card--front">
    <div class="card__texture" role="img" aria-label="Gold card face with fine geometric diamond pattern"></div>
    <div class="front__mark">
      <span class="mark__dot"></span>
      <span class="mark__name">VORASTI</span>
    </div>
    <div class="front__band">
      <div class="wordmark">VORASTI</div>
      <div class="wordmark__place">ITALY</div>
    </div>
  </section>

  <section class="card card--back">
    <div class="card__texture" role="img" aria-label="Dark card face with subtle embossed diamond pattern"></div>
    <div class="back__layout">
      <div class="identity">
        <div class="identity__mark">
          <span class="mark__dot"></span>
          <span class="mark__name">VORASTI</span>
        </div>
        <div class="identity__person">Paul Vorasti</div>
        <div class="identity__role">CEO and CO Founder</div>
      </div>
      <ul class="contacts">
        <li class="contacts__item">555-384-1962</li>
        <li class="contacts__item">555-384-1962</li>
        <li class="contacts__item">paul@vorasti.com</li>
        <li class="contacts__item">VORASTI.COM</li>
        <li class="contacts__item contacts__item--plain">4817 E Larkdale</li>
      </ul>
    </div>
  </section>
</main>
</body>
</html>
```